2026 Brenner Dust Control Municipal Advertisement

I need a professional print advertisement designed for our road dust control business for a 2026 municipal/public works publication.

Our company manufactures, supplies, delivers and applies liquid road dust suppressant products to municipalities, contractors and commercial customers across Ontario.

I will upload:

* Our new truck/application photo to use as the main image
* Our advertisement from last year as a reference for the general style and information

I would like the new advertisement to look modern, professional, industrial and appropriate for municipal/public works decision-makers. The truck photo should be the main visual.

Please include the following wording:

BRENNER DUST CONTROL PRODUCTS
418053 Ontario Limited
Based in Clinton, Ontario

ROAD DUST CONTROL PRODUCTS

Manufacturer & Distributor of Liquid Road Dust Suppressants

AVAILABLE CONCENTRATIONS

35%
Liquid Calcium Magnesium Chloride Solution

30%

20%

Bulk Supply • Delivery • Road Application

Supplying Municipalities, Contractors & Commercial Customers Across Ontario

519-730-2864
dwightbren418@mailvexo.com

Please make “ROAD DUST CONTROL PRODUCTS” one of the most prominent pieces of wording.

The 35%, 30% and 20% product concentrations should also be large, clear and easy to read.

“BRENNER DUST CONTROL PRODUCTS” should be prominently branded, with “418053 Ontario Limited” smaller underneath.

Please do not overcrowd the advertisement. It should be easy for someone flipping through a municipal publication to understand within a few seconds what we sell and how to contact us.

```html
<!DOCTYPE html>
<html lang="en">
<head>
<meta charset="utf-8">
<title>Brenner Dust Control Products – Road Dust Control</title>
<link rel="stylesheet" href="https://fonts.googleapis.com/css2?family=Russo+One&family=Oswald:wght@400;500;600;700&display=swap">
<style>
  :root {
    --ink: #0d0d0d;
    --white: #ffffff;
    --yellow: #f6c232;
    --road: #cdb89e;
    --field: #6e8f3c;
  }
  * { margin: 0; padding: 0; box-sizing: border-box; }
  html, body { width: 927px; height: 1200px; overflow: hidden; background: var(--white); }
  .ad { position: relative; width: 927px; height: 1200px; overflow: hidden; font-family: "Oswald", sans-serif; }

  .hero-photo {
    position: absolute; left: 0; top: 0; width: 927px; height: 1100px;
    background:
      linear-gradient(90deg, transparent 0 52%, rgba(236,230,222,.55) 62% 78%, transparent 90%),
      linear-gradient(180deg, var(--field) 0, #8fa55a 8%, var(--road) 22%, #c4ad92 60%, #bca288 100%);
  }
  .panel { position: absolute; left: 0; top: 0; }

  .brand-box { position: absolute; left: 29px; top: 38px; width: 751px; height: 125px; background: var(--white); padding: 7px 0 0 15px; }
  .brand-name { font-family: "Russo One", sans-serif; font-size: 64px; line-height: 56px; color: var(--ink); letter-spacing: 1px; white-space: nowrap; }
  .brand-sub { position: absolute; left: 29px; top: 163px; width: 506px; height: 34px; background: var(--yellow); color: var(--ink); font-weight: 500; font-size: 20px; line-height: 34px; padding-left: 17px; white-space: nowrap; }

  .headline { position: absolute; left: 29px; top: 198px; font-family: "Russo One", sans-serif; font-weight: 400; color: var(--white); font-size: 92px; line-height: 88px; white-space: nowrap; }
  .headline span { display: block; background: var(--ink); padding-left: 6px; }
  .headline .l1 { width: 597px; }
  .headline .l2, .headline .l3 { width: 480px; }

  .tagline { position: absolute; left: 37px; top: 466px; color: var(--yellow); font-weight: 500; font-size: 25px; line-height: 36px; white-space: nowrap; }

  .section-title { position: absolute; left: 26px; top: 552px; width: 401px; display: flex; align-items: center; gap: 14px; color: var(--white); font-size: 19px; }
  .section-title::before, .section-title::after { content: ""; flex: 1; height: 1px; background: var(--white); }

  .conc { position: absolute; width: 182px; }
  .conc-box { height: 120px; background: var(--white); border-radius: 14px; color: var(--ink); font-weight: 600; font-size: 96px; line-height: 120px; text-align: center; letter-spacing: -3px; white-space: nowrap; }
  .conc-label { margin-top: 10px; color: var(--yellow); font-size: 16.5px; line-height: 18px; text-align: center; }
  .c35 { left: 29px; top: 590px; }
  .c30 { left: 242px; top: 590px; }
  .c20 { left: 31px; top: 775px; }

  .customers { position: absolute; left: 258px; top: 783px; color: var(--ink); font-weight: 500; font-size: 20px; line-height: 26px; }

  .divider { position: absolute; left: 31px; top: 960px; width: 334px; height: 1px; background: var(--yellow); }

  .service { position: absolute; display: flex; align-items: center; gap: 8px; color: var(--yellow); font-weight: 500; font-size: 25px; line-height: 1; white-space: nowrap; }
  .service svg { fill: none; stroke: var(--white); stroke-width: 2; }
  .s-bulk { left: 24px; top: 986px; }
  .s-delivery { left: 219px; top: 986px; }
  .s-apply { left: 66px; top: 1032px; }

  .rule { position: absolute; left: 0; top: 1098px; width: 927px; height: 7px; background: var(--yellow); }
  .contact { position: absolute; top: 1121px; display: flex; align-items: center; gap: 14px; color: var(--ink); font-weight: 600; white-space: nowrap; }
  .contact svg { flex: none; }
  .phone { left: 34px; font-size: 43px; }
  .email { left: 379px; font-size: 33px; }
</style>
</head>
<body>
<div class="ad">
  <div class="hero-photo" role="img" aria-label="Aerial photo of a blue tanker truck applying liquid dust suppressant on a gravel road between green fields"></div>

  <svg class="panel" width="927" height="1100" viewBox="0 0 927 1100">
    <defs>
      <clipPath id="panel-shape">
        <path d="M0,0 H440 Q478,0 478,38 V464 H409 C455,560 505,650 505,770 C505,840 472,870 437,920 C410,960 400,1010 400,1098 H0 Z"/>
      </clipPath>
    </defs>
    <path d="M0,0 H440 Q478,0 478,38 V464 H409 C455,560 505,650 505,770 C505,840 472,870 437,920 C410,960 400,1010 400,1098 H0 Z" fill="var(--ink)"/>
    <path d="M409,466 C455,560 505,650 505,770 C505,840 472,870 437,920 C410,960 400,1010 400,1098" fill="none" stroke="var(--white)" stroke-width="3"/>
    <rect x="243" y="775" width="300" height="121" rx="14" fill="var(--white)" clip-path="url(#panel-shape)"/>
  </svg>

  <div class="brand-box">
    <div class="brand-name">BRENNER DUST<br>CONTROL PRODUCTS</div>
  </div>
  <div class="brand-sub">418053 ONTARIO LIMITED, BASED IN CLINTON, ONTARIO</div>

  <h1 class="headline">
    <span class="l1">ROAD DUST</span>
    <span class="l2">CONTROL</span>
    <span class="l3">PRODUCT</span>
  </h1>

  <p class="tagline">MANUFACTURER &amp; DISTRIBUTOR<br>OF LIQUID ROAD DUST SUPPRESSANTS</p>

  <div class="section-title">AVAILABLE CONCENTRATIONS</div>

  <div class="conc c35"><div class="conc-box">35%</div><p class="conc-label">LIQUID CALCIUM MAGNESIUM<br>CHLORIDE SOLUTION</p></div>
  <div class="conc c30"><div class="conc-box">30%</div><p class="conc-label">LIQUID CALCIUM MAGNESIUM<br>CHLORIDE SOLUTION</p></div>
  <div class="conc c20"><div class="conc-box">20%</div><p class="conc-label">LIQUID CALCIUM MAGNESIUM<br>CHLORIDE SOLUTION</p></div>

  <p class="customers">Supplying Municipalities,<br>Contractors &amp; Commercial<br>Customers<br>Across Ontario</p>

  <div class="divider"></div>

  <div class="service s-bulk">
    <svg width="46" height="34" viewBox="0 0 48 36"><rect x="3" y="12" width="30" height="14" rx="7"/><rect x="36" y="4" width="8" height="26"/><circle cx="26" cy="28" r="5"/><line x1="1" y1="30" x2="46" y2="30"/></svg>
    <span>BULK SUPPLY</span>
  </div>
  <div class="service s-delivery">
    <svg width="50" height="28" viewBox="0 0 54 30"><line x1="2" y1="8" x2="14" y2="8"/><line x1="4" y1="14" x2="16" y2="14"/><line x1="6" y1="20" x2="16" y2="20"/><rect x="18" y="4" width="20" height="18"/><path d="M38 10 H46 L51 16 V22 H38 Z"/><circle cx="25" cy="25" r="3"/><circle cx="45" cy="25" r="3"/></svg>
    <span>DELIVERY</span>
  </div>
  <div class="service s-apply">
    <svg width="58" height="42" viewBox="0 0 58 42"><rect x="17" y="4" width="24" height="22" rx="4"/><line x1="25" y1="4" x2="25" y2="26"/><line x1="33" y1="4" x2="33" y2="26"/><line x1="4" y1="28" x2="54" y2="28"/><path d="M8 32 L4 40 M8 32 L12 40 M29 32 L25 40 M29 32 L33 40 M50 32 L46 40 M50 32 L54 40"/></svg>
    <span>ROAD APPLICATION</span>
  </div>

  <div class="rule"></div>

  <div class="contact phone">
    <svg width="64" height="64" viewBox="0 0 64 64"><circle cx="32" cy="32" r="29" fill="none" stroke="var(--ink)" stroke-width="4"/><path d="M22 16 l7 9 -4 5 c2 5 5 8 10 10 l5 -4 9 7 -4 6 c-14 0 -28 -14 -28 -28 z" fill="var(--ink)"/></svg>
    <span>519-730-2864</span>
  </div>
  <div class="contact email">
    <svg width="64" height="64" viewBox="0 0 64 64"><circle cx="32" cy="32" r="29" fill="none" stroke="var(--ink)" stroke-width="4"/><rect x="16" y="21" width="32" height="22" fill="none" stroke="var(--ink)" stroke-width="3"/><path d="M16 21 L32 34 L48 21 M16 43 L28 31 M48 43 L36 31" fill="none" stroke="var(--ink)" stroke-width="3"/></svg>
    <span>DWIGHTBREN418@MAILVEXO.COM</span>
  </div>
</div>
</body>
</html>
```